Harlow Company Core Values

We are looking for an updated appearance to our Core Values with the addition of some descriptors to share with new hires, employees, and potential candidates

Requirements
Must have
• Core values and core value descriptors

```html
<!DOCTYPE html>
<html lang="en">
<head>
<meta charset="UTF-8">
<title>Harlow Company – Our Core Values</title>
<link rel="stylesheet" href="https://fonts.googleapis.com/css2?family=Mulish:wght@400;600;700;800&display=swap">
<style>
  :root {
    --backdrop: #e6e6e6;
    --paper: #ffffff;
    --brand-red: #a3222d;
    --ink: #262626;
    --body-ink: #333333;
    --rule: #3a3a3a;
    --dots: #6a6a6a;
  }
  * { box-sizing: border-box; margin: 0; padding: 0; }
  html, body {
    width: 1200px; height: 1000px; overflow: hidden;
    background: var(--backdrop);
    font-family: "Mulish", "Helvetica Neue", Arial, sans-serif;
  }
  .page {
    position: absolute; left: 230px; top: 28px;
    width: 740px; height: 944px;
    background: var(--paper);
  }
  .brand {
    position: absolute; top: 50px; left: 0; width: 100%;
    text-align: center;
    font-size: 38px; font-weight: 800; color: var(--brand-red);
    letter-spacing: 0.02em;
  }
  .tagline {
    position: absolute; top: 136px; left: 0; width: 100%;
    text-align: center;
    font-size: 12.5px; font-weight: 600; color: var(--brand-red);
    letter-spacing: 0.22em; text-transform: uppercase;
  }
  .page-title {
    position: absolute; top: 158px; left: 0; width: 100%;
    text-align: center;
    font-size: 30px; font-weight: 800; color: var(--ink);
    letter-spacing: 0.1em; text-transform: uppercase;
  }
  .value-card {
    position: absolute; width: 240px; height: 145px;
    border: 1.3px solid var(--rule);
    text-align: center;
  }
  .value-card--left { left: 124px; }
  .value-card--right { left: 374px; }
  .value-card--center { left: 248px; }
  .value-name {
    position: absolute; top: -17px; left: 50%; transform: translateX(-50%);
    width: 166px; height: 33px; line-height: 33px;
    background: var(--brand-red); color: #fff;
    border-radius: 17px;
    font-size: 11.5px; font-weight: 600; letter-spacing: 0.12em;
    text-transform: uppercase; white-space: nowrap;
  }
  .descriptors {
    list-style: none;
    position: absolute; top: 42px; left: 0; width: 100%;
    font-size: 12px; line-height: 19px; color: var(--body-ink);
  }
  .fill-line {
    position: absolute; top: 120px; left: 44px; width: 152px; height: 3px;
    border-bottom: 1.5px dotted var(--dots);
  }
  .footer-band {
    position: absolute; left: 124px; bottom: 0;
    width: 490px; height: 12px; background: var(--brand-red);
  }
</style>
</head>
<body>
  <main class="page">
    <div class="brand">Harlow</div>
    <p class="tagline">Keeping every journey moving since 1891</p>
    <h1 class="page-title">Our Core Values</h1>

    <section class="value-card value-card--left" style="top:243px">
      <h2 class="value-name">Respect Everyone</h2>
      <ul class="descriptors"><li>Be kind</li><li>Embrace each other’s differences</li><li>Healthy conflict</li></ul>
      <div class="fill-line"></div>
    </section>
    <section class="value-card value-card--right" style="top:243px">
      <h2 class="value-name">Aim for Excellence</h2>
      <ul class="descriptors"><li>Learn from our mistakes</li><li>Getting a little better everyday</li><li>Life long Learner</li></ul>
      <div class="fill-line"></div>
    </section>

    <section class="value-card value-card--left" style="top:416px">
      <h2 class="value-name">Take Care</h2>
      <ul class="descriptors"><li>Be safe</li><li>Be well</li><li>Look out for others</li></ul>
      <div class="fill-line"></div>
    </section>
    <section class="value-card value-card--right" style="top:416px">
      <h2 class="value-name">Communicate</h2>
      <ul class="descriptors"><li>Listen with intent</li><li>Ask questions</li><li>Think about delivery of message</li></ul>
      <div class="fill-line"></div>
    </section>

    <section class="value-card value-card--left" style="top:589px">
      <h2 class="value-name">Act Ethically</h2>
      <ul class="descriptors"><li>Respect</li><li>Doing the right thing</li><li>Understand what matters to others</li></ul>
      <div class="fill-line"></div>
    </section>
    <section class="value-card value-card--right" style="top:589px">
      <h2 class="value-name">Share Your Passion</h2>
      <ul class="descriptors"><li>Enjoy what you do</li><li>Help others</li><li>Positive outlook</li></ul>
      <div class="fill-line"></div>
    </section>

    <section class="value-card value-card--center" style="top:762px">
      <h2 class="value-name">Work Smart</h2>
      <ul class="descriptors"><li>Choose priorities</li><li>Focus</li><li>Seek to understand</li></ul>
      <div class="fill-line"></div>
    </section>

    <div class="footer-band"></div>
  </main>
</body>
</html>
```